Camp Thornbrook 2021 Magazine Design

We are for someone to design our annual magazine/newsletter. This is a print newsletter that is a total of 20 pages. It will need to be designed in a way that is easy to share with our printers. The designer will need to be someone who is creative and easy to work with.
For those interested in this project we ask that you design 4 to 6 pages for us to view. Once we select the designer we will want the rest created in a two-week time span. For those submitting a bid please include front cover, theme & dates, mission & vision, and Lend a Hand Forward.

This link will provide the layout of the newsletter https://files.pelmarsh.example/doc/7qTzR2kLpW9xVbN4cHsYd/view.

This link will provide you with the pictures that are needed and a few documents https://files.pelmarsh.example/folder/3hGvK8mQxZ5rLtP1wNcBj/view

Details:
20 pages long (including covers)
8.5 x 11

Please message me if you need any further details.

Target Market(s)

Our alumni base. Covers all ages

Requirements
Must have
• Spelled out in document
Nice to have
• Spelled out in document
Should not have
• Spelled out in document

```html
<!DOCTYPE html>
<html lang="en">
<head>
<meta charset="utf-8">
<title>Camp Thornbrook 2021 Magazine Spreads</title>
<link rel="stylesheet" href="https://fonts.googleapis.com/css2?family=Oswald:wght@400;500;600&family=Open+Sans:wght@400;600&display=swap">
<style>
:root{
  --bg:#f4f4f4;
  --paper:#ffffff;
  --ink:#333333;
  --green:#2f6f55;
  --teal:#2f6e63;
  --orange:#d9823f;
  --tan:#d4b47a;
  --forest:#1f3a2c;
  --mint:#bfe0cf;
  --salmon:#e98a6e;
  --gold:#d8bf85;
}
*{margin:0;padding:0;box-sizing:border-box}
html,body{width:1200px;height:1000px;overflow:hidden;background:var(--bg)}
body{position:relative;font-family:"Open Sans",sans-serif;color:var(--ink)}
.spread{position:absolute;display:flex;box-shadow:0 6px 14px rgba(0,0,0,.12)}
.page{position:relative;width:50%;height:100%;background:var(--paper);overflow:hidden}
.fill{position:absolute}
.body-text{font-size:4.2px;line-height:5.4px;color:#555}
.body-text p{margin-bottom:3px}
.heading{font-family:"Oswald",sans-serif;text-transform:uppercase}

/* cover */
.cover-spread{left:100px;top:135px;width:332px;height:225px}
.cover-collage{inset:0;background:linear-gradient(160deg,#b8612f 0%,#6e4a2a 30%,#d9a945 55%,#e8c352 75%,#9fb4d6 100%)}
.cover-year{position:absolute;left:0;right:0;top:86px;text-align:center;font-family:"Oswald",sans-serif;font-weight:600;font-size:34px;line-height:44px;color:#fff;letter-spacing:1px}

/* lend a hand */
.hand-spread{left:770px;top:148px;width:333px;height:225px}
.hand-photo{left:7px;top:20px;width:88px;height:150px;background:linear-gradient(180deg,#5f8a4a 0%,#7da05d 40%,#8c8a72 70%,#6a7b4e 100%)}
.hand-title{position:absolute;left:7px;top:26px;width:88px;text-align:center;font-family:"Oswald",sans-serif;font-weight:600;color:#fff;font-size:11px;line-height:12px}
.hand-date{position:absolute;left:7px;top:66px;width:88px;text-align:center;font-family:"Oswald",sans-serif;color:#fff;font-size:5px;letter-spacing:.5px}
.hand-col{position:absolute}

/* theme & dates */
.theme-spread{left:103px;top:645px;width:332px;height:230px}
.theme-left{background:linear-gradient(180deg,#ef9a8a 0%,#f3d6a8 35%,#f1e6b8 60%)}
.theme-right{background:linear-gradient(180deg,#f2eab8 0%,#bfe0cf 45%,#a9d6c2 100%)}
.forest{left:0;right:0;bottom:0;height:100px;background:linear-gradient(180deg,#2f4d3a 0%,var(--forest) 60%)}
.theme-emblem{left:35px;top:25px;width:102px;height:102px;border-radius:50%;background:radial-gradient(circle at 45% 40%,#a8a8a8 0%,#7c7c7c 55%,#5e5e5e 100%)}
.reg{position:absolute;left:12px;bottom:14px;width:150px;color:#fff;font-size:4.5px;line-height:6px;text-align:center}
.reg .heading{font-size:6px;margin-bottom:3px;letter-spacing:.5px}
.sessions{position:absolute;left:30px;top:22px;width:110px}
.sessions .heading{font-size:8px;color:var(--forest);letter-spacing:.5px;margin-bottom:5px}
.session-row{display:flex;justify-content:space-between;font-size:4.6px;line-height:7px;color:var(--salmon)}
.activities{position:absolute;left:12px;bottom:10px;width:140px;height:44px;background:#2c5a52;color:#fff}
.activities .heading{font-size:6px;text-align:center;padding-top:3px}
.activity-art{left:4px;top:4px;width:28px;height:36px;background:linear-gradient(135deg,#e2a043,#4b86b4)}
.activity-art2{right:4px;top:14px;width:24px;height:22px;background:linear-gradient(135deg,#e06a3d,#3d6db4)}
.activities .body-text{position:absolute;left:36px;top:14px;width:76px;color:#e8f0ec;font-size:3.6px;line-height:4.6px}
.price-badge{position:absolute;right:10px;top:128px;width:38px;height:38px;border-radius:50%;background:var(--gold);color:#fff;font-size:4px;line-height:5px;text-align:center;padding-top:10px}

/* mission & vision */
.mission-spread{left:770px;top:645px;width:333px;height:228px}
.photo-cross{left:0;top:0;width:100%;height:106px;background:linear-gradient(180deg,#6b9c4e 0%,#8db565 50%,#a69b7e 100%)}
.photo-gate{left:0;top:0;width:100%;height:106px;background:linear-gradient(180deg,#cfe0d6 0%,#7fae5d 45%,#4f8a3a 100%)}
.mission-title{position:absolute;left:8px;top:122px;font-family:"Oswald",sans-serif;font-weight:500;font-size:15px;line-height:20px;color:var(--green);white-space:nowrap}
.mission-cols{position:absolute;left:8px;top:146px;width:150px;display:flex;gap:6px}
.mission-cols .body-text{width:46px}
.box{position:absolute;color:#fff;padding:3px 4px}
.box .heading{font-size:5.5px;margin-bottom:2px}
.box .body-text{color:#fff;font-size:3.8px;line-height:4.8px}
.box-vision{left:13px;top:118px;width:63px;height:36px;background:var(--teal)}
.box-mission{left:80px;top:118px;width:72px;height:36px;background:var(--orange)}
.box-values{left:13px;top:157px;width:139px;height:58px;background:var(--tan)}
</style>
</head>
<body>

<section class="spread cover-spread">
  <div class="page"></div>
  <div class="page">
    <div class="fill cover-collage" role="img" aria-label="Collage of painted canoe paddles signed by campers from past summers"></div>
    <div class="cover-year">2020</div>
  </div>
</section>

<section class="spread hand-spread">
  <div class="page"></div>
  <div class="page">
    <div class="fill hand-photo" role="img" aria-label="Photo of a counselor hugging young campers outdoors"></div>
    <div class="hand-title">LEND A HAND FORWARD</div>
    <div class="hand-date">JULY 13TH – 17TH</div>
    <div class="hand-col body-text" style="left:100px;top:20px;width:62px">
      <p>Thornbrook has welcomed campers for decades, and every summer brings new faces, new friendships and new stories worth sharing with our alumni family.</p>
      <p>Each gift helps a child attend camp, grow in faith and find a place to belong among the pines.</p>
      <p>This spring we set a goal to fund fifty full scholarships, and our alumni answered with generous hearts and open hands.</p>
      <p>Thank you for keeping the campfire burning.</p>
    </div>
    <div class="hand-col body-text" style="left:7px;top:175px;width:42px">
      <p>This year we asked alumni to lend a hand forward so every camper who wants to come can join us.</p>
    </div>
    <div class="hand-col body-text" style="left:53px;top:175px;width:42px">
      <p>Your support made scholarships possible and kept our cabins full all summer long.</p>
    </div>
  </div>
</section>

<section class="spread theme-spread">
  <div class="page theme-left">
    <div class="fill forest" role="img" aria-label="Silhouette of pine forest at sunrise"></div>
    <div class="fill theme-emblem" role="img" aria-label="Resurrection 2021 summer theme emblem"></div>
    <div class="reg">
      <div class="heading">Registration and Other Information</div>
      <div>Registration opens on January 1, 2021</div>
      <div>Register online at campthornbrook.example</div>
      <div>Super Early Bird Discount ($50) if paid by March 1</div>
      <div>Early Bird Discount ($25) if paid by April 1</div>
    </div>
  </div>
  <div class="page theme-right">
    <div class="fill forest" style="height:80px" role="img" aria-label="Silhouette of pine forest"></div>
    <div class="sessions">
      <div class="heading">Sessions and Dates</div>
      <div class="session-row"><span>Session 1</span><span>Jun 6 – Jun 11</span><span>$325</span></div>
      <div class="session-row"><span>Junior Session</span><span>Jun 13 – Jun 16</span><span>$215</span></div>
      <div class="session-row"><span>Session 2</span><span>Jun 20 – Jun 25</span><span>$325</span></div>
      <div class="session-row"><span>Session 3</span><span>Jun 27 – Jul 2</span><span>$325</span></div>
      <div class="session-row"><span>Session 4</span><span>Jul 4 – Jul 9</span><span>$325</span></div>
      <div class="session-row"><span>Session 5</span><span>Jul 11 – Jul 16</span><span>$325</span></div>
      <div class="session-row"><span>Session 6</span><span>Jul 18 – Jul 23</span><span>$325</span></div>
      <div class="session-row"><span>Session 7</span><span>Jul 25 – Jul 30</span><span>$325</span></div>
      <div class="session-row"><span>Junior Session</span><span>Aug 1 – Aug 4</span><span>$215</span></div>
    </div>
    <div class="price-badge">Sibling<br>discount<br>$20 off</div>
    <div class="activities">
      <div class="fill activity-art" role="img" aria-label="Illustration of campers playing basketball"></div>
      <div class="fill activity-art2" role="img" aria-label="Illustration of camp games"></div>
      <div class="heading">Activities</div>
      <div class="body-text">Swimming, archery, canoeing, hiking, crafts, worship and games every day.</div>
    </div>
  </div>
</section>

<section class="spread mission-spread">
  <div class="page">
    <div class="fill photo-cross" role="img" aria-label="Photo of a wooden cross on a tree stump in the woods"></div>
    <div class="mission-title">OUR MISION AND VISION</div>
    <div class="mission-cols">
      <div class="body-text"><p>Camp Thornbrook exists to share faith with young people in a place set apart, where nature and friendship meet.</p></div>
      <div class="body-text"><p>We believe every child deserves a week to rest, play and listen, guided by counselors who care deeply.</p></div>
      <div class="body-text"><p>Our vision is to reconnect youth, families and community through service, worship and time outdoors together.</p></div>
    </div>
  </div>
  <div class="page">
    <div class="fill photo-gate" role="img" aria-label="Photo of two children walking toward the camp entrance gate"></div>
    <div class="box box-vision">
      <div class="heading">Our Vision</div>
      <div class="body-text">• Reconnecting Youth<br>• Reconnecting Community<br>• Reconnecting Families</div>
    </div>
    <div class="box box-mission">
      <div class="heading">Our Mission</div>
      <div class="body-text">We aim to share faith, grow leaders and build a community that serves others.</div>
    </div>
    <div class="box box-values">
      <div class="heading">Core Values</div>
      <div class="body-text">
        • We honor every camper as loved and valued.<br>
        • We provide a safe place to play and grow.<br>
        • We serve others with humble and joyful hearts.<br>
        • We care for creation and the land we share.<br>
        • We build lasting friendships across generations.<br>
        • We welcome every family with open arms.
      </div>
    </div>
  </div>
</section>

</body>
</html>
```